YouTube Banner for Bright Lantern Coding YouTube channel

I need a new YouTube banner designed that is more eye catching and communicates our value proposition which is helping JavaScript developers move from novice to expert. Here is the channel page: https://www.vidorama.net/channel/UCTLmPQZ7vDE42HnBkRaY3sq

Also, here is a link to our website in case that helps with the design. I would like things to tie together. www.brightlanterncoding.com

The image needs to include the tag line: Assisting your journey from novice to expert.

I've included the image of the original YouTube banner and an AI file of our logo.

MAKE SURE to follow the image size and file guidelines for YouTube banners on this page: https://help.tevrano.com/videohub/answer/5813460?hl=en

Target Market(s)

YouTube watchers wanting to increase their skills in JavaScript.

Industry/Entity Type

Youtube

Font styles to use
Serif
Sans Serif

Requirements
Must have
• Needs to tie in with my website and logo. Must be designed following the size and file guidelines provided by YouTube: https://help.tevrano.com/videohub/answer/5813460?hl=en

```html
<!DOCTYPE html>
<html lang="en">
<head>
<meta charset="utf-8">
<title>Bright Lantern Coding – Channel Banner</title>
<link rel="stylesheet" href="https://fonts.googleapis.com/css2?family=Questrial&family=Montserrat:wght@700&display=swap">
<style>
  :root {
    --page-white: #ffffff;
    --deep-teal: #02495a;
    --signal-red: #e00d00;
    --mustard: #d9b62f;
    --highlight-yellow: #fdd835;
    --ink: #111111;
    --logo-white: #ffffff;
  }
  html, body {
    margin: 0;
    padding: 0;
    width: 1200px;
    height: 1200px;
    overflow: hidden;
    background: var(--page-white);
  }
  .banner {
    position: relative;
    width: 1200px;
    height: 1200px;
  }
  .banner-shapes {
    position: absolute;
    inset: 0;
  }
  .tagline-line {
    position: absolute;
    margin: 0;
    font-family: "Questrial", "Helvetica Neue", Arial, sans-serif;
    font-size: 42px;
    line-height: 1;
    color: var(--ink);
    white-space: nowrap;
    letter-spacing: 0.3px;
  }
  .tagline-line--first { left: 268px; top: 547px; }
  .tagline-line--second { left: 264px; top: 599px; }
  .tagline-emphasis {
    position: absolute;
    left: 616px;
    top: 598px;
    font-family: "Montserrat", "Helvetica Neue", Arial, sans-serif;
    font-weight: 700;
    font-size: 40px;
    line-height: 1;
    color: var(--ink);
    white-space: nowrap;
  }
  .channel-name {
    position: absolute;
    left: 0;
    width: 1182px;
    top: 724px;
    text-align: center;
    font-family: "Questrial", "Helvetica Neue", Arial, sans-serif;
    font-size: 34px;
    line-height: 1;
    color: var(--logo-white);
    letter-spacing: 1px;
  }
</style>
</head>
<body>
<main class="banner">
  <svg class="banner-shapes" width="1200" height="1200" viewBox="0 0 1200 1200" aria-hidden="true">
    <rect class="teal-field" x="0" y="257" width="1182" height="666" fill="var(--deep-teal)"/>
    <rect class="red-stripe" x="0" y="493" width="1182" height="195" fill="var(--signal-red)"/>
    <path class="brace-frame" fill="var(--deep-teal)"
      d="M232,493 C222,493 224,505 224,520 L224,565 C224,580 214,588 198,590 C214,592 224,600 224,615 L224,668 C224,682 226,688 236,688 L948,688 C958,688 958,682 958,668 L958,615 C958,600 968,592 986,590 C968,588 958,580 958,565 L958,520 C958,505 960,493 950,493 Z"/>
    <rect class="tagline-panel" x="244" y="493" width="694" height="195" rx="14" fill="var(--mustard)"/>
    <rect class="emphasis-highlight" x="609" y="588" width="314" height="55" fill="var(--highlight-yellow)"/>
  </svg>

  <p class="tagline-line tagline-line--first">ASSISTING YOUR JOURNEY</p>
  <p class="tagline-line tagline-line--second">FROM NOVICE</p>
  <span class="tagline-emphasis">TO EXPERT</span>

  <div class="channel-name">Bright Lantern Coding</div>
</main>
</body>
</html>
```